Kestrel Signs Facebook Banner Design

Design a facebook banner for a sign company. I would like to have a modern approach to it.

Product Offering:
Signs
Banners
Decals
Commercial Wraps

```html
<!DOCTYPE html>
<html lang="en">
<head>
<meta charset="utf-8">
<title>Kestrel Signs – Facebook Banner</title>
<link rel="stylesheet" href="https://fonts.googleapis.com/css2?family=Antonio:wght@600;700&family=Montserrat:wght@500&display=swap">
<style>
  :root {
    --stage: #b3b3b3;
    --paper: #ffffff;
    --brand-red: #e93338;
    --ink: #545456;
    --tear-shadow: #d8d8d8;
  }
  * { margin: 0; padding: 0; box-sizing: border-box; }
  html, body { width: 1200px; height: 890px; overflow: hidden; }
  body { background: var(--stage); position: relative; }

  .banner {
    position: absolute;
    left: 125px; top: 237px;
    width: 949px; height: 416px;
    background: var(--paper);
    overflow: hidden;
  }
  .banner__tear { position: absolute; inset: 0; width: 949px; height: 416px; }

  .brand {
    position: absolute; left: 66px; top: 48px;
    font-family: "Antonio", sans-serif; font-weight: 700;
    color: var(--brand-red);
    font-size: 38px; line-height: 36px;
    letter-spacing: 2px; text-transform: uppercase;
  }

  .headline {
    font-family: "Antonio", sans-serif; font-weight: 600;
    text-transform: uppercase;
  }
  .headline__lead,
  .headline__main {
    position: absolute; left: 64px;
    display: block; white-space: nowrap; line-height: 1;
  }
  .headline__lead { top: 169px; color: var(--brand-red); font-size: 68px; letter-spacing: -0.3px; }
  .headline__main { top: 243px; color: var(--ink); font-size: 104px; letter-spacing: 0; }

  .offer-title {
    position: absolute; left: 582px; top: 92px;
    font-family: "Antonio", sans-serif; font-weight: 600;
    color: var(--brand-red); font-size: 40px; line-height: 40px;
    text-transform: uppercase; white-space: nowrap;
  }

  .offer-list {
    position: absolute; left: 584px; top: 156px;
    list-style: none;
    font-family: "Montserrat", sans-serif; font-weight: 500;
    color: var(--paper); font-size: 27px; letter-spacing: 0.5px;
    text-transform: uppercase; white-space: nowrap;
  }
  .offer-list li { display: flex; align-items: center; height: 48.5px; }
  .offer-list svg { width: 26px; height: 26px; margin-right: 12px; flex: none; }
</style>
</head>
<body>
  <section class="banner">
    <svg class="banner__tear" viewBox="0 0 949 416" aria-hidden="true">
      <polygon fill="var(--tear-shadow)" points="384,0 392,14 388,26 398,38 394,52 406,66 402,80 414,92 410,106 422,118 420,134 434,146 430,162 444,174 442,190 454,202 450,218 464,232 462,248 474,260 470,276 484,290 482,306 494,318 490,334 504,348 502,364 516,376 512,392 528,404 530,416 949,416 949,0"/>
      <polygon fill="var(--brand-red)" points="392,0 400,14 396,26 406,38 402,52 414,66 410,80 422,92 418,106 430,118 428,134 442,146 438,162 452,174 450,190 462,202 458,218 472,232 470,248 482,260 478,276 492,290 490,306 502,318 498,334 512,348 510,364 524,376 520,392 536,404 550,416 949,416 949,0"/>
      <polygon fill="var(--paper)" points="467,78 949,78 949,143 523,143"/>
    </svg>

    <div class="brand">Kestrel<br>Signs</div>

    <h1 class="headline">
      <span class="headline__lead">Make Yourself</span>
      <span class="headline__main">Stand Out</span>
    </h1>

    <h2 class="offer-title">Product Offering</h2>

    <ul class="offer-list">
      <li><svg viewBox="0 0 26 26"><path d="M22 11.5A9.5 9.5 0 1 1 17 4.6" fill="none" stroke="#fff" stroke-width="2.6" stroke-linecap="round"/><path d="M7.5 12.5l4.5 4.5L23 5" fill="none" stroke="#fff" stroke-width="2.8" stroke-linecap="round" stroke-linejoin="round"/></svg>Signs</li>
      <li><svg viewBox="0 0 26 26"><path d="M22 11.5A9.5 9.5 0 1 1 17 4.6" fill="none" stroke="#fff" stroke-width="2.6" stroke-linecap="round"/><path d="M7.5 12.5l4.5 4.5L23 5" fill="none" stroke="#fff" stroke-width="2.8" stroke-linecap="round" stroke-linejoin="round"/></svg>Banners</li>
      <li><svg viewBox="0 0 26 26"><path d="M22 11.5A9.5 9.5 0 1 1 17 4.6" fill="none" stroke="#fff" stroke-width="2.6" stroke-linecap="round"/><path d="M7.5 12.5l4.5 4.5L23 5" fill="none" stroke="#fff" stroke-width="2.8" stroke-linecap="round" stroke-linejoin="round"/></svg>Decals</li>
      <li><svg viewBox="0 0 26 26"><path d="M22 11.5A9.5 9.5 0 1 1 17 4.6" fill="none" stroke="#fff" stroke-width="2.6" stroke-linecap="round"/><path d="M7.5 12.5l4.5 4.5L23 5" fill="none" stroke="#fff" stroke-width="2.8" stroke-linecap="round" stroke-linejoin="round"/></svg>Commercial Wraps</li>
    </ul>
  </section>
</body>
</html>
```